New Innovative Counselling and psychotherapy Service needs Business Card design

Keep it simple and professional. On one side, just company name and logo (perhaps in all blue) and maybe a tag line.

On other side (all white) my name and Qualifications in centre

Industry/Entity Type

Health And Wellness

Contact Information for Business Card

Derek Hollis
Counsellor & Psychotherapist
BSc (Psychol.), BA, Dip. (Couns. & Psych.), PG.Cert (CBT), MGVrA, NWTF

I will also require Mobile no, Email and web site address of which I'll pass on to final designer.

Font styles to use
Sans Serif

Requirements
Must have
• My Logo Only and please use the colours in logo that is in it.
Should not have
• Any other images

```html
<!DOCTYPE html>
<html lang="en">
<head>
<meta charset="utf-8">
<title>Kindred Path – Business Card</title>
<link href="https://fonts.googleapis.com/css2?family=Raleway:wght@400;500&family=Roboto:wght@400;500;700&display=swap" rel="stylesheet">
<style>
  :root{
    --canvas:#e9ecef;
    --brand-blue:#4aa7dc;
    --brand-blue-deep:#1d7fab;
    --brand-blue-mid:#2a97cc;
    --ink:#2f3237;
    --ink-soft:#4a4d52;
    --paper:#fbfbfb;
  }
  *{margin:0;padding:0;box-sizing:border-box}
  html,body{width:1200px;height:800px;overflow:hidden}
  body{background:var(--canvas);display:flex;align-items:center;justify-content:center;gap:48px;font-family:'Roboto',Arial,sans-serif}
  .card{width:536px;height:306px;position:relative;overflow:hidden;box-shadow:0 10px 28px rgba(0,0,0,.18)}

  /* front */
  .card-front{background:var(--brand-blue);display:flex;align-items:center;justify-content:center;gap:22px}
  .card-front .brand-mark{width:70px;height:70px;border-radius:50%;background:#fff}
  .card-front .brand-name{font-family:'Raleway',Arial,sans-serif;font-weight:400;font-size:40px;color:#fff;letter-spacing:.5px}

  /* back */
  .card-back{background:var(--paper)}
  .back-brand{position:absolute;top:36px;right:34px;display:flex;align-items:center;gap:14px}
  .back-brand .brand-mark{width:44px;height:44px;border-radius:50%;background:var(--brand-blue-mid)}
  .back-brand .brand-name{font-family:'Raleway',Arial,sans-serif;font-weight:500;font-size:25px;color:var(--ink)}
  .holder{position:absolute;left:40px;top:96px}
  .holder-name{font-weight:700;font-size:22px;color:var(--brand-blue-mid)}
  .holder-role{font-weight:500;font-size:11.5px;color:var(--ink);margin-top:6px}
  .holder-quals{font-size:9px;color:var(--ink-soft);margin-top:4px;line-height:1.35;width:230px}
  .contacts{position:absolute;left:40px;top:182px;list-style:none}
  .contacts li{display:flex;align-items:center;gap:14px;height:24px;font-size:15px;font-weight:500;color:var(--ink)}
  .contacts .icon{width:20px;height:20px;background:var(--brand-blue-mid);display:flex;align-items:center;justify-content:center}
  .contacts .icon svg{width:13px;height:13px}
  .band{position:absolute;left:0;right:0;bottom:0;height:20px;background:linear-gradient(90deg,var(--brand-blue-mid),var(--brand-blue-deep))}
</style>
</head>
<body>
  <section class="card card-front" aria-label="Card front">
    <span class="brand-mark"></span>
    <span class="brand-name">Kindred Path</span>
  </section>

  <section class="card card-back" aria-label="Card back">
    <div class="back-brand">
      <span class="brand-mark"></span>
      <span class="brand-name">Kindred Path</span>
    </div>

    <div class="holder">
      <h1 class="holder-name">Derek Hollis</h1>
      <p class="holder-role">Counsellor &amp; Psychotherapist</p>
      <p class="holder-quals">BSc (Psychol.), BA, Dip. (Couns. &amp; Psych.),<br>PG.Cert (CBT), MGVrA, NWTF</p>
    </div>

    <ul class="contacts">
      <li><span class="icon"><svg viewBox="0 0 24 24" fill="#fff"><path d="M6.6 10.8a15 15 0 0 0 6.6 6.6l2.2-2.2c.3-.3.7-.4 1-.2 1.1.4 2.3.6 3.6.6.6 0 1 .4 1 1V20c0 .6-.4 1-1 1A17 17 0 0 1 3 4c0-.6.4-1 1-1h3.5c.6 0 1 .4 1 1 0 1.3.2 2.5.6 3.6.1.3 0 .7-.2 1z"/></svg></span>Your contact no. here</li>
      <li><span class="icon"><svg viewBox="0 0 24 24" fill="none" stroke="#fff" stroke-width="2"><rect x="3" y="5" width="18" height="14"/><path d="M3 6l9 7 9-7"/></svg></span>youremailid@mailbox.com</li>
      <li><span class="icon"><svg viewBox="0 0 24 24" fill="none" stroke="#fff" stroke-width="2"><circle cx="12" cy="12" r="9"/><path d="M3 12h18M12 3c3 3 3 15 0 18M12 3c-3 3-3 15 0 18"/></svg></span>www.yourwebaddress.com</li>
      <li><span class="icon"><svg viewBox="0 0 24 24" fill="#fff"><path d="M12 2a7 7 0 0 0-7 7c0 5 7 13 7 13s7-8 7-13a7 7 0 0 0-7-7zm0 9.5A2.5 2.5 0 1 1 12 6.5a2.5 2.5 0 0 1 0 5z"/></svg></span>your address here</li>
    </ul>

    <div class="band"></div>
  </section>
</body>
</html>
```